Brightkeel Logistics - Cards and Logo

We need a logo and card design for a Logistics company located in Chicago. Our competitors are KTR and Qorvan. We would like to see designs that incorporate a logo that shows all ways in terms of direction. The colors would be Electric Blue, Grays, Blacks and White. I like how Moko has a badge type logo that is strong and clean. Velmora also has a strong font that is futuristic. The final design should communicate we are a strong and technological type of company. I show a picture of the colors we like from a moko cooler.

```html
<!DOCTYPE html>
<html lang="en">
<head>
<meta charset="utf-8">
<title>Brightkeel Logistics – Business Cards</title>
<link rel="stylesheet" href="https://fonts.googleapis.com/css2?family=Montserrat:wght@600;700;800&family=Open+Sans:wght@600&display=swap">
<style>
:root{
  --stage:#1a1d20;
  --card:#0b0d10;
  --blue:#17a4e0;
  --blue-deep:#1673c4;
  --gray:#9c9c9a;
  --gray-light:#c9cacc;
  --map:#2c4454;
}
*{margin:0;padding:0;box-sizing:border-box}
html,body{width:1200px;height:1000px;overflow:hidden;background:var(--stage)}
.stage{position:relative;width:1200px;height:1000px}
.card{position:absolute;width:524px;height:299px;background:var(--card);overflow:hidden;box-shadow:0 8px 24px rgba(0,0,0,.45)}
.card--tl{left:62px;top:186px}
.card--tr{left:615px;top:186px}
.card--bl{left:62px;top:515px}
.card--br{left:615px;top:515px}

/* front */
.world-map{position:absolute;left:36px;top:8px;width:460px;height:282px;border-radius:40% 46% 38% 44%;
  background:radial-gradient(ellipse at 50% 45%,rgba(44,68,84,.75) 0%,rgba(44,68,84,.35) 55%,rgba(44,68,84,0) 75%)}
.brand{display:flex;align-items:center;gap:10px;font-family:"Montserrat",sans-serif;font-weight:800;color:var(--blue);letter-spacing:.5px;white-space:nowrap}
.brand__mark{width:14px;height:14px;background:var(--blue)}
.card__front-brand{position:absolute;left:0;right:0;top:132px;justify-content:center;font-size:30px}

/* back */
.card__back-brand{position:absolute;left:23px;top:48px;font-size:23px}
.person{position:absolute;right:12px;top:118px;text-align:right}
.person__name{font-family:"Montserrat",sans-serif;font-weight:700;font-size:20px;color:var(--gray);letter-spacing:1px;padding-right:23px;position:relative}
.person__name::after{content:"";position:absolute;right:0;top:11px;width:15px;height:3px;background:var(--blue)}
.person__title{font-family:"Open Sans",sans-serif;font-weight:600;font-size:16px;color:var(--blue);padding-right:23px;margin-top:2px}
.divider{position:absolute;left:13px;top:152px;width:323px;height:3px;background:var(--gray)}
.contact{position:absolute;display:flex;align-items:flex-start;gap:12px;font-family:"Open Sans",sans-serif;font-weight:600;font-size:14px;line-height:18px;color:var(--gray-light)}
.contact__icon{width:23px;height:23px;border-radius:3px;background:var(--blue);flex:none;display:flex;align-items:center;justify-content:center}
.contact__icon svg{width:15px;height:15px}
.contact span{padding-top:2px}
.c-mobile{left:22px;top:171px}
.c-phone{left:22px;top:208px}
.c-mail{left:22px;top:243px}
.c-web{left:280px;top:171px}
.c-addr{left:280px;top:208px}
.accent-band{position:absolute;left:0;bottom:0;width:524px;height:19px}
</style>
</head>
<body>
<main class="stage">

  <!-- front, top left -->
  <section class="card card--tl">
    <div class="world-map" role="img" aria-label="Dotted world map in muted steel blue"></div>
    <div class="brand card__front-brand"><span class="brand__mark"></span>BRIGHTKEEL LOGISTICS</div>
  </section>

  <!-- back, top right -->
  <section class="card card--tr">
    <div class="brand card__back-brand"><span class="brand__mark"></span>BRIGHTKEEL LOGISTICS</div>
    <div class="person">
      <div class="person__name">DANE ROURKE</div>
      <div class="person__title">Managing Partner</div>
    </div>
    <div class="divider"></div>
    <div class="contact c-mobile"><i class="contact__icon"><svg viewBox="0 0 16 16"><rect x="4" y="1" width="8" height="14" rx="1.5" fill="none" stroke="#0b0d10" stroke-width="1.6"/><circle cx="8" cy="12.5" r="1" fill="#0b0d10"/></svg></i><span>312-555-0147</span></div>
    <div class="contact c-phone"><i class="contact__icon"><svg viewBox="0 0 16 16"><path d="M2 6c0-2 3-3 6-3s6 1 6 3l-2 1-1-2H5L4 7z" fill="#0b0d10"/><rect x="4" y="8" width="8" height="6" rx="1" fill="#0b0d10"/></svg></i><span>773-555-0182</span></div>
    <div class="contact c-mail"><i class="contact__icon"><svg viewBox="0 0 16 16"><rect x="1.5" y="3.5" width="13" height="9" fill="none" stroke="#0b0d10" stroke-width="1.5"/><path d="M1.5 3.5 8 9l6.5-5.5" fill="none" stroke="#0b0d10" stroke-width="1.5"/></svg></i><span>Dane.rourke@brightkeellogistics.com</span></div>
    <div class="contact c-web"><i class="contact__icon"><svg viewBox="0 0 16 16" fill="none" stroke="#0b0d10" stroke-width="1.3"><circle cx="8" cy="8" r="6.5"/><ellipse cx="8" cy="8" rx="3" ry="6.5"/><path d="M1.5 8h13M3 4.5h10M3 11.5h10"/></svg></i><span>www.brightkeellogistics.com</span></div>
    <div class="contact c-addr"><i class="contact__icon"><svg viewBox="0 0 16 16"><path d="M8 1a4.5 4.5 0 0 0-4.5 4.5C3.5 9 8 15 8 15s4.5-6 4.5-9.5A4.5 4.5 0 0 0 8 1z" fill="#0b0d10"/><circle cx="8" cy="5.5" r="1.7" fill="#17a4e0"/></svg></i><span>418 W Harlan Ave, Suite 112<br>Chicago, IL 60610</span></div>
    <svg class="accent-band" viewBox="0 0 524 19" preserveAspectRatio="none">
      <defs>
        <linearGradient id="bandGray1" x1="0" x2="1"><stop offset="0" stop-color="#6f7072"/><stop offset="1" stop-color="#b5b5b3"/></linearGradient>
        <linearGradient id="bandBlue1" x1="0" x2="1"><stop offset="0" stop-color="#14b2ea"/><stop offset="1" stop-color="#1673c4"/></linearGradient>
      </defs>
      <polygon points="0,0 93,0 101,19 0,19" fill="url(#bandGray1)"/>
      <polygon points="97,0 524,0 524,19 105,19" fill="url(#bandBlue1)"/>
    </svg>
  </section>

  <!-- back, bottom left -->
  <section class="card card--bl">
    <div class="brand card__back-brand"><span class="brand__mark"></span>BRIGHTKEEL LOGISTICS</div>
    <div class="person">
      <div class="person__name">EVAN HOLLOWAY</div>
      <div class="person__title">Managing Partner</div>
    </div>
    <div class="divider"></div>
    <div class="contact c-mobile"><i class="contact__icon"><svg viewBox="0 0 16 16"><rect x="4" y="1" width="8" height="14" rx="1.5" fill="none" stroke="#0b0d10" stroke-width="1.6"/><circle cx="8" cy="12.5" r="1" fill="#0b0d10"/></svg></i><span>630-555-0129</span></div>
    <div class="contact c-phone"><i class="contact__icon"><svg viewBox="0 0 16 16"><path d="M2 6c0-2 3-3 6-3s6 1 6 3l-2 1-1-2H5L4 7z" fill="#0b0d10"/><rect x="4" y="8" width="8" height="6" rx="1" fill="#0b0d10"/></svg></i><span>773-555-0182</span></div>
    <div class="contact c-mail"><i class="contact__icon"><svg viewBox="0 0 16 16"><rect x="1.5" y="3.5" width="13" height="9" fill="none" stroke="#0b0d10" stroke-width="1.5"/><path d="M1.5 3.5 8 9l6.5-5.5" fill="none" stroke="#0b0d10" stroke-width="1.5"/></svg></i><span>Evan.holloway@brightkeellogistics.com</span></div>
    <div class="contact c-web"><i class="contact__icon"><svg viewBox="0 0 16 16" fill="none" stroke="#0b0d10" stroke-width="1.3"><circle cx="8" cy="8" r="6.5"/><ellipse cx="8" cy="8" rx="3" ry="6.5"/><path d="M1.5 8h13M3 4.5h10M3 11.5h10"/></svg></i><span>www.brightkeellogistics.com</span></div>
    <div class="contact c-addr"><i class="contact__icon"><svg viewBox="0 0 16 16"><path d="M8 1a4.5 4.5 0 0 0-4.5 4.5C3.5 9 8 15 8 15s4.5-6 4.5-9.5A4.5 4.5 0 0 0 8 1z" fill="#0b0d10"/><circle cx="8" cy="5.5" r="1.7" fill="#17a4e0"/></svg></i><span>418 W Harlan Ave, Suite 112<br>Chicago, IL 60610</span></div>
    <svg class="accent-band" viewBox="0 0 524 19" preserveAspectRatio="none">
      <defs>
        <linearGradient id="bandGray2" x1="0" x2="1"><stop offset="0" stop-color="#6f7072"/><stop offset="1" stop-color="#b5b5b3"/></linearGradient>
        <linearGradient id="bandBlue2" x1="0" x2="1"><stop offset="0" stop-color="#14b2ea"/><stop offset="1" stop-color="#1673c4"/></linearGradient>
      </defs>
      <polygon points="0,0 93,0 101,19 0,19" fill="url(#bandGray2)"/>
      <polygon points="97,0 524,0 524,19 105,19" fill="url(#bandBlue2)"/>
    </svg>
  </section>

  <!-- front, bottom right -->
  <section class="card card--br">
    <div class="world-map" role="img" aria-label="Dotted world map in muted steel blue"></div>
    <div class="brand card__front-brand"><span class="brand__mark"></span>BRIGHTKEEL LOGISTICS</div>
  </section>

</main>
</body>
</html>
```